Business card design needed

We are 2 artists starting up a studio by the water in Sydney ...where we can work and display our art...would like the back ground to be Navy and white stripe...nautical...and the name The Paint Hut to be bold and the main wording...not nautical...if possible thought the A for art could be an easel ...ie the capital A using the cross bar as the platform that paint would be circles of colour....would like the main wording in Black but the easel A in colour
Hope u are able to help
thanku Lorna Vesk
as I will be away in a week for 4 weeks could u please send all info to Mira Colbins email....she can contact me and we can go ahead asap....

Artists

THE PAINT HUT

Hallorans Oar House
The Reach..17 Kellaby Rd..Dunrook 2091 Sydney

Mir Colbin..0437819025..miracolbin@mailnest.example
Lorn Vesk...0429573816..lvesk@harborlink.example

```html
<!DOCTYPE html>
<html lang="en">
<head>
<meta charset="utf-8">
<title>The Paint Hut – Business Card</title>
<link rel="stylesheet" href="https://fonts.googleapis.com/css2?family=Cinzel:wght@700&family=Aldrich&display=swap">
<style>
  :root {
    --page-bg: #1c1c1e;
    --navy: #14254f;
    --white: #ffffff;
    --ink: #111111;
    --text-navy: #14254f;
    --paint: #d6336c;
  }
  * { margin: 0; padding: 0; box-sizing: border-box; }
  html, body {
    width: 877px;
    height: 1200px;
    overflow: hidden;
    background: var(--page-bg);
  }
  .canvas {
    width: 877px;
    height: 1200px;
    display: flex;
    align-items: center;
    justify-content: center;
  }
  .card {
    position: relative;
    width: 877px;
    height: 546px;
    overflow: hidden;
    background: var(--white);
    display: flex;
    flex-direction: column;
  }
  .card__stripes {
    height: 70px;
    flex: none;
    background: repeating-linear-gradient(180deg,
      var(--navy) 0, var(--navy) 14px,
      var(--white) 14px, var(--white) 28px);
  }
  .card__stripes--bottom {
    background: repeating-linear-gradient(0deg,
      var(--navy) 0, var(--navy) 14px,
      var(--white) 14px, var(--white) 28px);
  }
  .card__content {
    flex: 1;
    display: flex;
    flex-direction: column;
    align-items: center;
    justify-content: center;
    text-align: center;
    color: var(--text-navy);
    font-family: 'Aldrich', sans-serif;
  }
  .brand {
    display: flex;
    align-items: center;
    gap: 18px;
  }
  .brand__dot {
    width: 26px;
    height: 26px;
    border-radius: 50%;
    background: var(--paint);
    flex: none;
  }
  .brand__name {
    font-family: 'Cinzel', serif;
    font-weight: 700;
    font-size: 62px;
    letter-spacing: 2px;
    line-height: 1;
    color: var(--ink);
  }
  .address {
    font-size: 22px;
    line-height: 34px;
    letter-spacing: 1.5px;
    margin-top: 26px;
  }
  .contacts {
    display: flex;
    justify-content: center;
    gap: 56px;
    margin-top: 28px;
  }
  .contact__name {
    font-size: 26px;
    letter-spacing: 1px;
    color: var(--ink);
    line-height: 1.3;
  }
  .contact__phone,
  .contact__email {
    font-size: 20px;
    letter-spacing: 0.5px;
    line-height: 1.5;
  }
  .contact__email {
    text-decoration: underline;
    text-underline-offset: 4px;
  }
</style>
</head>
<body>
  <main class="canvas">
    <section class="card" aria-label="The Paint Hut business card">
      <div class="card__stripes" aria-hidden="true"></div>
      <div class="card__content">
        <div class="brand">
          <span class="brand__dot" aria-hidden="true"></span>
          <h1 class="brand__name">THE PAINT HUT</h1>
        </div>
        <p class="address">HALLORANS OAR HOUSE THE REACH<br>17 KELLABY RD, DUNROOK 2091 SYDNEY</p>
        <div class="contacts">
          <div class="contact">
            <p class="contact__name">MIR COLBIN</p>
            <p class="contact__phone">0437819025</p>
            <p class="contact__email">miracolbin@mailnest.example</p>
          </div>
          <div class="contact">
            <p class="contact__name">LORN VESK</p>
            <p class="contact__phone">0429573816</p>
            <p class="contact__email">lvesk@harborlink.example</p>
          </div>
        </div>
      </div>
      <div class="card__stripes card__stripes--bottom" aria-hidden="true"></div>
    </section>
  </main>
</body>
</html>
```